Copperfield Roofing Co. business card design

I am a Roofing contractor in Texas. The name of my company is Copperfield Roofing Co. I also offer a few other services (Christmas light installation, gutters, fencing, pressure washing). However my main gig is roofing. Storm restoration and knowledge of the insurance claim process is my specialty.

My colors are black, red and white. I’d like something pretty simple and clean. Modern looking but with a splash of this red tartan pattern.

I have another version of my logo being edited at the moment where the little top part of the F in roofing that’s currently tartan will be changed to just solid red to make it more visible. So if that’s something you can change in your mock up great. But I can provide the full version once the contest is complete

Target Market(s)

Homeowners

Industry/Entity Type

Roofing

Contact Information for Business Card

Derek Pruitt. 682-555-0193. www.copperfield roofing.co Derek@copperfieldroofing.co

Colors
EB3D1F
EC4F4E
F09395
F8D3D4
FCEDEE

Requirements
Nice to have
• Maybe instead of a business address. I could say serving all DFW Texas or something like that. And maybe add a line somewhere saying deductible assistance? Just a thought

```html
<!DOCTYPE html>
<html lang="en">
<head>
<meta charset="utf-8">
<title>Copperfield Roofing Co. – Business Card</title>
<link rel="stylesheet" href="https://fonts.googleapis.com/css2?family=Lato:wght@400;700;900&family=Michroma&display=swap">
<style>
  :root {
    --stage: #3a3a3a;
    --red: #d10a0a;
    --red-dark: #8e0606;
    --red-deep: #6a0303;
    --ink: #1c1c1c;
    --white: #ffffff;
  }
  * { margin: 0; padding: 0; box-sizing: border-box; }
  html, body { width: 1200px; height: 1122px; overflow: hidden; }
  body {
    background: var(--stage);
    font-family: "Lato", sans-serif;
    position: relative;
  }
  .card {
    position: absolute;
    left: 180px;
    width: 840px;
    height: 480px;
    overflow: hidden;
  }
  .card--front { top: 60px; background: var(--red); }
  .card--back { top: 582px; background: var(--ink); }

  .tartan-field {
    position: absolute; inset: 0;
    background:
      linear-gradient(90deg, transparent 0 78%, rgba(0,0,0,.28) 78% 90%, transparent 90%),
      linear-gradient(180deg, transparent 0 14%, rgba(0,0,0,.28) 14% 30%, transparent 30%),
      linear-gradient(135deg, var(--red) 0%, #c00808 55%, var(--red-dark) 100%);
  }

  .brand {
    position: absolute;
    display: flex; flex-direction: column; align-items: center;
    text-align: center;
  }
  .brand__mark { border-radius: 50%; }
  .brand__name {
    font-family: "Lato", sans-serif;
    font-weight: 900;
    text-transform: uppercase;
    line-height: 1.05;
    letter-spacing: .04em;
  }
  .card--front .brand { left: 0; right: 0; top: 70px; }
  .card--front .brand__mark { width: 170px; height: 170px; background: var(--white); margin-bottom: 28px; }
  .card--front .brand__name { color: var(--white); font-size: 46px; }

  .back-art { position: absolute; inset: 0; }
  .card--back .brand { left: 560px; width: 280px; top: 110px; }
  .card--back .brand__mark { width: 130px; height: 130px; background: var(--red); margin-bottom: 22px; }
  .card--back .brand__name { color: var(--red); font-size: 28px; }

  .contact { position: absolute; left: 62px; top: 118px; color: var(--white); }
  .contact__name {
    font-family: "Michroma", sans-serif;
    color: var(--red);
    font-size: 36px;
    text-transform: uppercase;
    letter-spacing: .02em;
  }
  .contact__title { font-size: 24px; font-weight: 700; margin-top: 4px; }
  .contact__list { list-style: none; margin-top: 34px; }
  .contact__item {
    display: flex; align-items: flex-start; gap: 14px;
    font-size: 20px; line-height: 1.25; margin-bottom: 12px;
  }
  .contact__item--phone { font-size: 26px; font-weight: 700; }
  .contact__icon { width: 20px; height: 20px; flex: none; margin-top: 3px; fill: var(--red); }
</style>
</head>
<body>

<section class="card card--front" aria-label="Card front">
  <div class="tartan-field" role="img" aria-label="Red tartan plaid pattern background"></div>
  <div class="brand">
    <div class="brand__mark"></div>
    <p class="brand__name">Copperfield<br>Roofing Co.</p>
  </div>
</section>

<section class="card card--back" aria-label="Card back">
  <svg class="back-art" viewBox="0 0 840 480" width="840" height="480" aria-hidden="true">
    <polygon points="470,0 484,0 600,480 572,480" fill="var(--red-dark)"/>
    <polygon points="484,0 496,0 616,480 600,480" fill="var(--red)"/>
    <polygon points="496,0 840,0 840,480 616,480" fill="var(--white)"/>
    <polygon points="500,0 506,0 624,480 616,480" fill="var(--red)"/>
  </svg>

  <div class="contact">
    <h1 class="contact__name">Derek Pruitt</h1>
    <p class="contact__title">Founder &amp; CEO</p>
    <ul class="contact__list">
      <li class="contact__item">
        <svg class="contact__icon" viewBox="0 0 24 24"><path d="M12 2a7 7 0 0 0-7 7c0 5 7 13 7 13s7-8 7-13a7 7 0 0 0-7-7zm0 9.5A2.5 2.5 0 1 1 12 6.5a2.5 2.5 0 0 1 0 5z"/></svg>
        <span>123 Anywhere St<br>Any City, State 12345</span>
      </li>
      <li class="contact__item contact__item--phone">
        <svg class="contact__icon" viewBox="0 0 24 24"><path d="M6.6 10.8a15 15 0 0 0 6.6 6.6l2.2-2.2a1 1 0 0 1 1-.25 11.4 11.4 0 0 0 3.6.6 1 1 0 0 1 1 1V20a1 1 0 0 1-1 1A17 17 0 0 1 3 4a1 1 0 0 1 1-1h3.5a1 1 0 0 1 1 1c0 1.25.2 2.45.6 3.6a1 1 0 0 1-.25 1z"/></svg>
        <span>682-555-0193</span>
      </li>
      <li class="contact__item">
        <svg class="contact__icon" viewBox="0 0 24 24"><path d="M2 5h20v14H2zm2 2v.5l8 5 8-5V7z"/></svg>
        <span>Derek@copperfieldroofing.co</span>
      </li>
      <li class="contact__item">
        <svg class="contact__icon" viewBox="0 0 24 24"><path d="M12 2a10 10 0 1 0 0 20 10 10 0 0 0 0-20zm6.9 6h-3a15 15 0 0 0-1.3-4A8 8 0 0 1 18.9 8zM12 4c.8 1.2 1.5 2.5 1.9 4h-3.8c.4-1.5 1.1-2.8 1.9-4zM4.3 14a8 8 0 0 1 0-4h3.4a16 16 0 0 0 0 4zm.8 2h3a15 15 0 0 0 1.3 4A8 8 0 0 1 5.1 16zm3-8h-3a8 8 0 0 1 4.3-4A15 15 0 0 0 8.1 8zM12 20c-.8-1.2-1.5-2.5-1.9-4h3.8c-.4 1.5-1.1 2.8-1.9 4zm2.3-6H9.7a14 14 0 0 1 0-4h4.6a14 14 0 0 1 0 4zm.3 6a15 15 0 0 0 1.3-4h3a8 8 0 0 1-4.3 4zm1.7-6a16 16 0 0 0 0-4h3.4a8 8 0 0 1 0 4z"/></svg>
        <span>www.copperfield roofing.co</span>
      </li>
    </ul>
  </div>

  <div class="brand">
    <div class="brand__mark"></div>
    <p class="brand__name">Copperfield<br>Roofing Co.</p>
  </div>
</section>

</body>
</html>
```